Business Card Design

We are a residential half way house for the addict ,the alcoholic and dual diagnosed in recovery.
i house both men and woman age 18+

Industry/Entity Type

Residential

```html
<!DOCTYPE html>
<html lang="en">
<head>
<meta charset="utf-8">
<title>Harbor Light Family Sober House – Business Card</title>
<link rel="stylesheet" href="https://fonts.googleapis.com/css2?family=Poppins:wght@300;400;600&display=swap">
<style>
  :root {
    --page-bg: #eeeeee;
    --card-grey: #6d6e71;
    --accent-orange: #e65a32;
    --disc-grey: #d8d8da;
    --ring-white: #efefef;
    --name-ink: #3a3a3c;
    --role-ink: #8e8e91;
    --contact-ink: #ffffff;
  }
  html, body {
    margin: 0;
    padding: 0;
    width: 1200px;
    height: 758px;
    overflow: hidden;
    background: var(--page-bg);
  }
  .canvas {
    position: relative;
    width: 1200px;
    height: 758px;
    display: flex;
    align-items: center;
    justify-content: center;
  }
  .business-card {
    position: relative;
    width: 840px;
    height: 480px;
    overflow: hidden;
    border-radius: 4px;
    box-shadow: 0 2px 10px rgba(0, 0, 0, 0.12);
    font-family: "Poppins", sans-serif;
  }
  .card-shapes {
    position: absolute;
    inset: 0;
    width: 100%;
    height: 100%;
  }
  .card-shapes .base { fill: var(--card-grey); }
  .card-shapes .accent { fill: var(--accent-orange); }
  .card-shapes .ring { fill: var(--ring-white); }
  .card-shapes .disc { fill: var(--disc-grey); }
  .identity {
    position: absolute;
    left: 0;
    right: 0;
    top: 108px;
    text-align: center;
  }
  .person-name {
    margin: 0;
    font-weight: 600;
    font-size: 66px;
    line-height: 1;
    letter-spacing: -0.5px;
    color: var(--name-ink);
  }
  .person-role {
    margin: 14px 0 0;
    font-weight: 300;
    font-size: 28px;
    line-height: 1;
    color: var(--role-ink);
  }
  .contact-block {
    position: absolute;
    left: 0;
    right: 0;
    top: 338px;
    text-align: center;
    font-weight: 400;
    font-size: 19px;
    line-height: 1.55;
    color: var(--contact-ink);
  }
  .contact-block p { margin: 0; }
</style>
</head>
<body>
  <main class="canvas">
    <article class="business-card">
      <svg class="card-shapes" viewBox="0 0 840 480" aria-hidden="true">
        <rect class="base" x="0" y="0" width="840" height="480"/>
        <path class="accent" d="M0 0 H840 V200 Q520 210 0 330 Z"/>
        <circle class="ring" cx="420" cy="-78" r="394"/>
        <circle class="disc" cx="420" cy="-78" r="378"/>
      </svg>

      <header class="identity">
        <h1 class="person-name">Marina Delgado</h1>
        <p class="person-role">Owner (15 yrs. in recovery)</p>
      </header>

      <address class="contact-block">
        <p class="contact-address">Harbor Light Family Sober House Inc. 2480 Palm Grove Rd. Seabrook,Fla 33400</p>
        <p class="contact-phone">Phone: (555) 014-2281 (555) 014-2282 | Fax - 555-019-4470</p>
        <p class="contact-email">Email: marinadelgado@example.com</p>
      </address>
    </article>
  </main>
</body>
</html>
```